ARC VOLLEY Business Card Project

I'd like to request a business card design for the new company I've launched.
The name of the company is "ARC VOLLEY" an indoor unmanned tennis practice facility.
We would like to see designs that use our brand identity color in the logo I've attached.
We hope to get the design with modern, luxurious and elegant tone and manner.
We hope the logo should not be too big.

Business card must have elements as below:
- Logo (One of the logos I've attached)
- Name (In Korean Text) : 박 서 윤
- Title (In Korean Text) : 대표
- Phone Number : 010-8472-3916
- Email Address : seoyun.park@arcvolley-example.co.kr
- Website : www.arcvolley-example.co.kr
- Instagram : arcvolley
- Address (In Korean text) : 경기도 용인시 수지구 풍덕천로 456 미래타워 5층 501호, 502호

Target Market(s)

Tennis amateurs in 20 to 40s

Industry/Entity Type

Sports, Hobby

Contact Information for Business Card

- Logo (One of the logos I've attached) - Name (In Korean Text) : 박 서 윤 - Title (In Korean Text) : 대표 - Phone Number : 010-8472-3916 - Email Address : seoyun.park@arcvolley-example.co.kr - Website : www.arcvolley-example.co.kr - Instagram : arcvolley - Address (In Korean text) : 경기도 용인시 수지구 풍덕천로 456 미래타워 5층 501호, 502호

Font styles to use
Sans Serif

Requirements
Must have
• Double sided
Nice to have
• Logo with intaglio or relief embossing
Should not have
• Logo should not be too big.

```html
<!DOCTYPE html>
<html lang="ko">
<head>
<meta charset="utf-8">
<title>ARC VOLLEY Business Card</title>
<link rel="stylesheet" href="https://fonts.googleapis.com/css2?family=Noto+Sans+KR:wght@400;700&family=Noto+Serif:wght@400&display=swap">
<style>
  :root {
    --backdrop: #8e8e8e;
    --card-white: #ffffff;
    --brand-green: #2e5239;
    --ink-dark: #333333;
    --ink-text: #2a2a2a;
    --ink-muted: #555555;
  }
  html, body {
    margin: 0;
    padding: 0;
    width: 1200px;
    height: 1200px;
    overflow: hidden;
    background: var(--backdrop);
  }
  .canvas {
    position: relative;
    width: 1200px;
    height: 1200px;
  }
  .card {
    position: absolute;
    left: 281px;
    width: 641px;
    height: 366px;
    border-radius: 19px;
    overflow: hidden;
  }
  .card--front { top: 195px; background: var(--card-white); }
  .card--back {
    top: 639px;
    background: var(--brand-green);
    display: flex;
    align-items: center;
    justify-content: center;
  }

  .brand-mark {
    position: absolute;
    top: 40px;
    right: 26px;
    display: flex;
    align-items: center;
    gap: 6px;
    font-family: "Noto Serif", serif;
    font-size: 11px;
    letter-spacing: 1px;
    color: var(--brand-green);
  }
  .brand-mark__dot {
    width: 10px;
    height: 10px;
    border-radius: 50%;
    background: var(--brand-green);
  }

  .identity {
    position: absolute;
    right: calc(641px - 243px);
    top: 140px;
    text-align: right;
    font-family: "Noto Sans KR", sans-serif;
    font-weight: 400;
  }
  .identity__name {
    font-size: 34px;
    line-height: 38px;
    color: var(--brand-green);
    letter-spacing: -1px;
  }
  .identity__title {
    font-size: 22px;
    line-height: 28px;
    color: var(--ink-muted);
  }

  .divider {
    position: absolute;
    left: 268px;
    top: 138px;
    width: 1px;
    height: 85px;
    background: var(--brand-green);
  }

  .contacts {
    position: absolute;
    left: 296px;
    top: 142px;
    margin: 0;
    padding: 0;
    list-style: none;
    font-family: "Noto Serif", serif;
    font-size: 14px;
    color: var(--ink-text);
  }
  .contacts__item {
    display: flex;
    align-items: center;
    height: 19.5px;
  }
  .contacts__icon {
    width: 10px;
    height: 10px;
    margin-right: 8px;
    flex: none;
  }

  .address {
    position: absolute;
    left: 0;
    right: 0;
    top: 308px;
    display: flex;
    justify-content: center;
    align-items: center;
    gap: 5px;
    font-family: "Noto Sans KR", sans-serif;
    font-weight: 700;
    font-size: 12.5px;
    color: var(--ink-dark);
  }
  .address__icon { width: 9px; height: 12px; }

  .back-name {
    font-family: "Noto Serif", serif;
    font-weight: 400;
    font-size: 42px;
    letter-spacing: 2px;
    color: var(--card-white);
  }
</style>
</head>
<body>
<div class="canvas">

  <section class="card card--front" aria-label="Business card front">
    <div class="brand-mark"><span class="brand-mark__dot"></span>ARC VOLLEY</div>

    <div class="identity">
      <div class="identity__name">박서윤</div>
      <div class="identity__title">대표</div>
    </div>

    <div class="divider"></div>

    <ul class="contacts">
      <li class="contacts__item">
        <svg class="contacts__icon" viewBox="0 0 10 10"><path d="M2 1 L4 3 L3 4 Q4 6 6 7 L7 6 L9 8 L8 9.5 Q2 9 0.5 2 Z" fill="#2e5239"/></svg>
        010-8472-3916
      </li>
      <li class="contacts__item">
        <svg class="contacts__icon" viewBox="0 0 10 10"><rect x="0.5" y="2" width="9" height="6.5" fill="#2e5239"/><path d="M0.8 2.3 L5 5.6 L9.2 2.3" stroke="#fff" stroke-width="0.9" fill="none"/></svg>
        seoyun.park@arcvolley-example.co.kr
      </li>
      <li class="contacts__item">
        <svg class="contacts__icon" viewBox="0 0 10 10"><circle cx="5" cy="5" r="4.3" fill="none" stroke="#2e5239" stroke-width="1.2"/><path d="M3 2.5 Q4.5 4 3.5 6 L5 8 M6.5 2 Q6 4 7.5 5" stroke="#2e5239" stroke-width="1.2" fill="none"/></svg>
        www.arcvolley-example.co.kr
      </li>
      <li class="contacts__item">
        <svg class="contacts__icon" viewBox="0 0 10 10"><rect x="1" y="1" width="8" height="8" rx="2.2" fill="none" stroke="#2e5239" stroke-width="1.1"/><circle cx="5" cy="5" r="1.8" fill="none" stroke="#2e5239" stroke-width="1.1"/></svg>
        arcvolley
      </li>
    </ul>

    <div class="address">
      <svg class="address__icon" viewBox="0 0 9 12"><path d="M4.5 0.5 A4 4 0 0 1 8.5 4.5 C8.5 7.5 4.5 11.5 4.5 11.5 C4.5 11.5 0.5 7.5 0.5 4.5 A4 4 0 0 1 4.5 0.5 Z" fill="#2e5239"/><circle cx="4.5" cy="4.5" r="1.5" fill="#fff"/></svg>
      경기도 용인시 수지구 풍덕천로 456 미래타워 5층 501호, 502호
    </div>
  </section>

  <section class="card card--back" aria-label="Business card back">
    <div class="back-name">ARC VOLLEY</div>
  </section>

</div>
</body>
</html>
```